Banner Ad Design Project

I place ads in Clickrow and also get traffic from sites like http://www.wellspringlistings.example.au/ to offer our free meditation CD and report at http://quietmindful.example.au/get-the-free-meditation-cd
We need new designs to improve this campaign.
Target Market(s)
40+ year old women, looking for personal growth or help with stress, depression, anxiety, sleep problems, health issues, memory/concentration issues
Industry/Entity Type
Campaign

```html
<!DOCTYPE html>
<html lang="en">
<head>
<meta charset="utf-8">
<title>Quiet Mindful – Banner Set</title>
<link rel="stylesheet" href="https://fonts.googleapis.com/css2?family=Arimo:wght@700&family=Roboto+Condensed:wght@500;700&display=swap">
<style>
  :root {
    --stage: #2b2b2b;
    --frame: #ffffff;
    --blue-light: #3f86e3;
    --blue-mid: #1f5fc9;
    --blue-deep: #163f9e;
    --orange: #f7860d;
    --ink: #111111;
    --white: #ffffff;
    --disc-a: #dfe9f3;
    --disc-b: #8fb4d8;
  }
  * { box-sizing: border-box; margin: 0; padding: 0; }
  html, body { width: 1200px; height: 800px; overflow: hidden; }
  body { background: var(--stage); position: relative; font-family: "Arimo", Arial, sans-serif; }

  .banner { position: absolute; background: var(--frame); padding: 6px; }
  .banner__field { position: relative; width: 100%; height: 100%; overflow: hidden; }
  .banner__shapes { position: absolute; inset: 0; width: 100%; height: 100%; }
  .banner__shapes .sky { fill: url(#blueSky); }
  .banner__shapes .cap { fill: var(--white); }
  .banner__shapes .rim { fill: none; stroke: var(--orange); stroke-width: 4; }
  .banner__shapes .swoosh { fill: var(--orange); }

  .brand, .offer, .hook, .price { position: absolute; }
  .brand { font-family: "Arimo", Arial, sans-serif; font-weight: 700; color: var(--ink); line-height: 1.12; }
  .offer { font-family: "Roboto Condensed", "Arial Narrow", sans-serif; font-weight: 500; color: var(--white); line-height: 1.2; text-shadow: 0 1px 2px rgba(0,0,0,.35); }
  .hook { font-family: "Arimo", Arial, sans-serif; font-weight: 700; color: var(--white); line-height: 1.25; text-shadow: 0 1px 2px rgba(0,0,0,.35); }
  .hook--narrow { font-family: "Roboto Condensed", "Arial Narrow", sans-serif; font-weight: 500; }
  .price { font-family: "Arimo", Arial, sans-serif; font-weight: 700; color: var(--ink); white-space: nowrap; }
  .price__amount { font-size: 1.9em; vertical-align: -0.12em; }

  .disc { position: absolute; border-radius: 50%; background: radial-gradient(circle at 50% 50%, var(--white) 0 9%, var(--disc-a) 10% 45%, var(--disc-b) 100%); box-shadow: 0 0 0 2px rgba(255,255,255,.6); }

  /* Skyscraper */
  .banner--sky { left: 95px; top: 28px; width: 195px; height: 724px; }
  .banner--sky .brand { left: 12px; top: 14px; font-size: 27px; }
  .banner--sky .offer { left: 0; right: 0; top: 152px; text-align: center; font-size: 22px; }
  .banner--sky .disc { left: 39px; top: 246px; width: 96px; height: 96px; }
  .banner--sky .hook { right: 6px; top: 400px; text-align: right; font-size: 22px; line-height: 1.6; }
  .banner--sky .price { left: 22px; top: 584px; font-size: 21px; line-height: 1.3; white-space: normal; }
  .banner--sky .price__label { display: block; }
  .banner--sky .price__label span { display: block; padding-left: 42px; }
  .banner--sky .price__amount { display: block; text-align: right; padding-right: 6px; font-size: 44px; }

  /* Medium rectangle */
  .banner--rect { left: 497px; top: 52px; width: 447px; height: 375px; }
  .banner--rect .brand { left: 24px; top: 6px; font-size: 29px; }
  .banner--rect .disc { left: 290px; top: 72px; width: 98px; height: 98px; }
  .banner--rect .offer { left: 14px; top: 118px; font-family: "Arimo", Arial, sans-serif; font-weight: 700; font-size: 21px; line-height: 1.3; }
  .banner--rect .hook { left: 100px; top: 188px; text-align: center; font-size: 25px; line-height: 1.25; }
  .banner--rect .hook small { font-size: 19px; display: block; }
  .banner--rect .price { right: 16px; top: 300px; font-size: 27px; }
  .banner--rect .price__amount { font-size: 46px; }

  /* Small leaderboard */
  .banner--strip { left: 348px; top: 474px; width: 774px; height: 100px; }
  .banner--strip .brand { left: 24px; top: 12px; font-size: 21px; }
  .banner--strip .offer { left: 226px; top: 8px; font-size: 24px; }
  .banner--strip .hook { left: 200px; top: 36px; text-align: center; font-size: 17px; width: 260px; }
  .banner--strip .price { right: 16px; top: 22px; font-size: 23px; }
  .banner--strip .price__amount { font-size: 40px; }

  /* Wide leaderboard */
  .banner--wide { left: 315px; top: 604px; width: 861px; height: 154px; }
  .banner--wide .brand { left: 22px; top: 14px; font-size: 28px; }
  .banner--wide .offer { left: 292px; top: 12px; font-size: 33px; }
  .banner--wide .hook { left: 236px; top: 80px; text-align: center; font-size: 24px; line-height: 1.15; }
  .banner--wide .hook small { font-size: 19px; display: block; }
  .banner--wide .price { right: 14px; top: 78px; font-size: 23px; }
  .banner--wide .price__amount { font-size: 50px; }
</style>
</head>
<body>
<svg width="0" height="0" style="position:absolute" aria-hidden="true">
  <defs>
    <linearGradient id="blueSky" x1="0" y1="0" x2="0.6" y2="1">
      <stop offset="0" stop-color="#3f86e3"/>
      <stop offset="0.55" stop-color="#1f5fc9"/>
      <stop offset="1" stop-color="#163f9e"/>
    </linearGradient>
  </defs>
</svg>

<section class="banner banner--sky" aria-label="Skyscraper banner">
  <div class="banner__field">
    <svg class="banner__shapes" viewBox="0 0 183 712" preserveAspectRatio="none" aria-hidden="true">
      <rect class="sky" width="183" height="712"/>
      <path class="cap" d="M0 0H183V92Q110 118 0 100Z"/>
      <path class="rim" d="M0 100Q110 118 183 92"/>
      <path class="swoosh" d="M0 600Q80 545 183 548V712H0Z"/>
    </svg>
    <p class="brand">Quiet<br>Mindful</p>
    <p class="offer">FREE Meditation CD<br>and Special Report</p>
    <div class="disc" role="img" aria-label="Meditation CD disc showing a woman seated in a meditation pose"></div>
    <p class="hook hook--narrow">How to Meditate<br>Deeper Than<br>a Zen Monk!</p>
    <p class="price"><span class="price__label">Valued<span>at</span></span><span class="price__amount">$37</span></p>
  </div>
</section>

<section class="banner banner--rect" aria-label="Medium rectangle banner">
  <div class="banner__field">
    <svg class="banner__shapes" viewBox="0 0 435 363" preserveAspectRatio="none" aria-hidden="true">
      <rect class="sky" width="435" height="363"/>
      <path class="cap" d="M0 0H270Q300 80 150 98Q60 104 0 90Z"/>
      <path class="rim" d="M0 90Q60 104 150 98Q300 80 270 0"/>
      <path class="swoosh" d="M110 363Q190 292 435 272V363Z"/>
    </svg>
    <p class="brand">Quiet<br>Mindful</p>
    <div class="disc" role="img" aria-label="Meditation CD disc showing a woman seated in a meditation pose"></div>
    <p class="offer">FREE Meditation CD<br>and Special Report</p>
    <p class="hook">How to Meditate<small>Deeper Than a Zen Monk!</small></p>
    <p class="price">Value at <span class="price__amount">$37</span></p>
  </div>
</section>

<section class="banner banner--strip" aria-label="Small leaderboard banner">
  <div class="banner__field">
    <svg class="banner__shapes" viewBox="0 0 762 88" preserveAspectRatio="none" aria-hidden="true">
      <rect class="sky" width="762" height="88"/>
      <path class="cap" d="M0 0H210Q215 70 60 84H0Z"/>
      <path class="rim" d="M0 86Q200 80 212 0"/>
      <path class="swoosh" d="M480 88Q560 20 762 0V88Z"/>
    </svg>
    <p class="brand">Quiet<br>Mindful</p>
    <p class="offer">FREE Meditation CD and Special Report</p>
    <p class="hook">How to Meditate<br>Deeper Than a Zen Monk!</p>
    <p class="price">Value at <span class="price__amount">$37</span></p>
  </div>
</section>

<section class="banner banner--wide" aria-label="Wide leaderboard banner">
  <div class="banner__field">
    <svg class="banner__shapes" viewBox="0 0 849 142" preserveAspectRatio="none" aria-hidden="true">
      <rect class="sky" width="849" height="142"/>
      <path class="cap" d="M0 0H275Q290 95 80 104H0Z"/>
      <path class="rim" d="M0 106Q290 100 278 0"/>
      <path class="swoosh" d="M560 142Q650 50 849 40V142Z"/>
    </svg>
    <p class="brand">Quiet<br>Mindful</p>
    <p class="offer">FREE Meditation CD and Special Report</p>
    <p class="hook">How to Meditate<small>Deeper Than a Zen Monk!</small></p>
    <p class="price">Valued at <span class="price__amount">$37</span></p>
  </div>
</section>
</body>
</html>
```